Logo Name:
Reach Agility Massage
Company Intro:
Reach Massage Therapy is another approach to functional movement and injury prevention. Reach Massage Therapy can increase range of motion, increase athletic performance, help with posture, decrease stress & aid in muscle recovery.
Instructions:
Two years ago, all of you created my current logo and I love it, however I am now a license Massage Therapist (LMT) #MA40518 and by law any advertising must include that I am an LMT #MA40518, so I need to change my logo to include Massage, LMT & my license number #MA40518. My current logo (see attached) has Flexibility, Mobility and Performance & I want include Sports Massage. I want it clean, easy to read, soft to eyes but have a pop. the color format ca change, I am open to ideas.

Ill need to add my updated commercial address, listed below. I must also have LMT #MA40518 on the lower right or lower left of the from of the card. Reach Agilely Massage is located at: Ember Palm Therapeutics 4731 NE 6th Avenue Corvell Heights, FL 33418 Cell: 508.739.2056
Update, I forgot to mention, my name Dean J. Holcomb needs to be under logo. Mt cell phone number would go under the address.
Sports Massage or just massage needs to be apart of the heading as its an additional service I provide to stretch therapy. I am a massage therapist but my specialty is Sports Massage. In the smaller heading with Flexibility Mobility Performance, please add Structural Integration

```html
<!DOCTYPE html>
<html lang="en">
<head>
<meta charset="utf-8">
<title>Reach Agility Massage – Business Card</title>
<link rel="stylesheet" href="https://fonts.googleapis.com/css2?family=Montserrat:ital,wght@0,700;0,800;1,600;1,700;1,800&family=Roboto+Condensed:ital,wght@1,700&display=swap">
<style>
  :root {
    --brand-blue: #0b3f8e;
    --brand-orange: #f2621a;
    --paper: #ffffff;
  }
  * { margin: 0; padding: 0; box-sizing: border-box; }
  html, body {
    width: 1200px;
    height: 900px;
    overflow: hidden;
    background: var(--paper);
  }
  .card {
    position: relative;
    width: 1200px;
    height: 900px;
    background: var(--paper);
    font-family: "Montserrat", sans-serif;
    color: var(--brand-blue);
  }
  .card > * { position: absolute; line-height: 1; white-space: nowrap; }

  .brand-name {
    left: 60px;
    width: 1080px;
    top: 140px;
    text-align: center;
    font-weight: 800;
    font-size: 100px;
    line-height: 112px;
    color: var(--brand-blue);
  }
  .tagline {
    left: 50px;
    width: 1100px;
    top: 389px;
    text-align: center;
    font-family: "Roboto Condensed", sans-serif;
    font-weight: 700;
    font-style: italic;
    font-size: 34px;
    letter-spacing: 0.5px;
  }
  .divider {
    left: 60px;
    top: 467px;
    width: 760px;
    height: 3px;
    background: var(--brand-orange);
  }
  .license {
    left: 843px;
    top: 455px;
    font-weight: 700;
    font-style: italic;
    font-size: 29px;
    letter-spacing: 4px;
    color: var(--brand-orange);
  }
  .person-name {
    left: 0;
    width: 1156px;
    top: 485px;
    text-align: center;
    font-weight: 800;
    font-size: 38px;
    letter-spacing: 1px;
  }
  .person-title {
    left: 0;
    width: 1140px;
    top: 543px;
    text-align: center;
    font-weight: 700;
    font-style: italic;
    font-size: 27px;
    letter-spacing: 1.5px;
  }
  .business {
    left: 60px;
    top: 615px;
    font-weight: 800;
    font-size: 33px;
    letter-spacing: 1px;
  }
  .address {
    left: 54px;
    top: 665px;
    font-weight: 600;
    font-style: italic;
    font-size: 26px;
    line-height: 41px;
    letter-spacing: 0.5px;
  }
  .phone {
    left: 54px;
    top: 756px;
    font-weight: 800;
    font-style: italic;
    font-size: 26px;
  }
  .online {
    right: 96px;
    top: 665px;
    text-align: right;
    font-style: italic;
    font-size: 26px;
    line-height: 41px;
  }
  .online .web { font-weight: 700; }
  .online .email { font-weight: 600; }
</style>
</head>
<body>
  <main class="card">
    <h1 class="brand-name">REACH AGILITY<br>MASSAGE</h1>
    <p class="tagline">FLEXIBILITY • MOBILITY • PERFORMANCE • STRUCTURAL INTEGRATION</p>
    <div class="divider"></div>
    <p class="license">LMT #MA40518</p>

    <h2 class="person-name">Dean J. Holcomb</h2>
    <p class="person-title">Licensed Massage Therapist</p>

    <h3 class="business">Ember Palm Therapeutics</h3>
    <address class="address">
      4731 NE 6th Avenue,<br>
      Corvell Heights,&nbsp; FL 33418
    </address>
    <p class="phone">Cell: 508.739.2056</p>

    <div class="online">
      <div class="web">www.reachagility.com</div>
      <div class="email">reachagility@gmail.com</div>
    </div>
  </main>
</body>
</html>
```